Electrician Company Website Design

I am looking to get a website designed only. I do not need it converted ot html. I simply need the design in a psd format. I have my own team for the conversion. The website is for an electrician company called Bramblecourt electric. I have created a txt document with the project parameters and specifics. I have also uploaded their logo in all avaible formats. It's a zip file.

Number of Pages Required

1 page

```html
<!DOCTYPE html>
<html lang="en">
<head>
<meta charset="utf-8">
<title>Bramblecourt Electric</title>
<link href="https://fonts.googleapis.com/css2?family=Poppins:wght@400;500;600&family=Roboto+Condensed:wght@700&display=swap" rel="stylesheet">
<style>
:root{
  --blue:#1e63b4;
  --blue-dark:#174f93;
  --red:#a3212a;
  --red-bright:#b22630;
  --ink:#111111;
  --text:#444444;
  --light:#f5f5f5;
  --line:#d0d0d0;
  --white:#ffffff;
}
*{margin:0;padding:0;box-sizing:border-box}
html,body{width:1200px;height:4093px;overflow:hidden}
body{position:relative;background:var(--white);font-family:'Poppins',sans-serif;color:var(--text);font-size:13px;line-height:1.75}
.abs{position:absolute}
.head{font-family:'Roboto Condensed',sans-serif;font-weight:700;color:var(--ink);text-transform:uppercase;letter-spacing:.5px}
.head .accent{color:var(--red)}
.btn{position:absolute;display:flex;align-items:center;justify-content:center;background:var(--red);color:var(--white);border-radius:20px;font-size:13px}

/* top bar */
.topbar{left:0;top:0;width:1200px;height:67px;background:var(--blue)}
.brand{left:60px;top:9px;display:flex;align-items:center;gap:10px;height:50px;z-index:3}
.brand-mark{width:46px;height:46px;border-radius:50%;background:var(--white);flex:none}
.brand-name{font-weight:600;font-size:15px;color:var(--white);text-transform:uppercase;letter-spacing:1px;line-height:1.3}
.hotline{left:810px;top:14px;display:flex;gap:12px;color:var(--white)}
.hotline-icon{width:30px;height:30px;border-radius:50%;background:var(--red);display:flex;align-items:center;justify-content:center}
.hotline small{display:block;font-size:11px;line-height:1.4}
.hotline strong{font-size:15px;font-weight:600;line-height:1.2}
.nav{left:0;top:67px;width:1200px;height:44px;background:var(--white)}
.nav a{position:absolute;top:0;height:44px;display:flex;align-items:center;font-size:12px;color:var(--ink);text-decoration:none}
.nav a.active{background:var(--red);color:var(--white);justify-content:center;width:89px}

/* hero */
.hero{left:0;top:111px;width:1200px;height:564px;background:linear-gradient(90deg,#ececec,#dedede)}
.hero-photo{left:556px;top:111px;width:644px;height:564px;background:linear-gradient(135deg,#d8d8d8 0%,#bfc3c7 45%,#3c4a66 75%,#2a3550 100%)}
.hero-title{left:60px;top:262px;font-size:58px;line-height:66px}
.hero-text{left:60px;top:405px;width:500px;font-size:13px;line-height:23px}

/* connect band */
.connect{left:0;top:675px;width:1200px;height:73px;background:var(--red)}
.connect-label{left:0;top:675px}
.connect-text{left:60px;top:690px;color:var(--white);font-size:16px;font-weight:500;line-height:21px}
.field{position:absolute;top:694px;height:37px;background:var(--white);border-radius:19px;font-size:12px;color:#555;display:flex;align-items:center;padding-left:20px}
.field-select{justify-content:space-between;padding-right:16px}
.connect-submit{left:1049px;top:694px;width:90px;height:37px;background:var(--blue)}

/* welcome */
.welcome-photo{left:60px;top:826px;width:450px;height:374px;border-radius:12px;background:linear-gradient(135deg,#9aa3ad,#5d6a7a 55%,#2e4b7a)}
.play{left:487px;top:991px;width:42px;height:42px;border-radius:50%;background:var(--blue);border:4px solid var(--white);display:flex;align-items:center;justify-content:center}
.welcome-title{left:617px;top:842px;font-size:34px;line-height:45px}
.welcome-text{left:617px;top:938px;width:495px;font-size:13px;line-height:22.6px}

/* services */
.services-wave{left:0;top:1280px;width:1200px;height:740px}
.services-title{left:0;top:1400px;width:1200px;text-align:center;color:var(--white);font-size:34px}
.services-intro{left:0;top:1450px;width:1200px;text-align:center;color:var(--white);font-size:13px;line-height:23px}
.service{position:absolute;top:1522px;width:340px;text-align:center;color:var(--white)}
.service-photo{width:238px;height:238px;border-radius:50%;border:5px solid var(--blue);margin:0 auto;background:linear-gradient(135deg,#b8c2cc,#4a6a93 60%,#1f3b66)}
.service h3{font-family:'Roboto Condensed',sans-serif;font-size:16px;margin-top:22px;line-height:22px}
.service p{font-size:13px;line-height:23px;margin-top:6px}
.service .more{color:#3f86d6;font-size:12px;margin-top:10px;display:flex;gap:6px;justify-content:center;align-items:center}

/* service area */
.area-title{left:60px;top:2145px;font-size:34px}
.area-text{left:60px;top:2192px;width:560px;font-size:13px;line-height:23px}
.town{position:absolute;display:flex;gap:10px;align-items:center;font-family:'Roboto Condensed',sans-serif;font-weight:700;color:var(--ink);font-size:16px}
.area-map{left:771px;top:2086px;width:368px;height:412px;background:linear-gradient(170deg,#e4cc9a 0%,#dcbf86 55%,#a9bde0 100%)}

/* gallery */
.gallery-bg{left:0;top:2540px;width:1200px;height:620px}
.gallery-title{left:0;top:2666px;width:1200px;text-align:center;font-size:34px}
.gallery-text{left:0;top:2713px;width:1200px;text-align:center;font-size:13px;line-height:23px}
.shot{position:absolute;top:2782px;height:247px;border-radius:4px}
.arrow{position:absolute;top:2890px;width:32px;height:32px;border-radius:50%;display:flex;align-items:center;justify-content:center}

/* contact */
.contact-title{left:0;top:3232px;width:1200px;text-align:center;font-size:34px}
.contact-sub{left:0;top:3278px;width:1200px;text-align:center;font-size:12px}
.input{position:absolute;left:249px;width:339px;height:35px;border:1px solid var(--line);font-size:12px;color:#666;padding:6px 14px}
.input.focus{border-color:var(--red)}

/* footer */
.footer-wave{left:0;top:3650px;width:1200px;height:400px}
.foot-brand{left:60px;top:3810px;display:flex;align-items:center;gap:10px}
.foot-brand .brand-mark{width:54px;height:54px}
.foot-brand span{font-weight:600;font-size:17px;color:var(--white);text-transform:uppercase;letter-spacing:1px;line-height:1.3}
.foot-head{position:absolute;top:3790px;color:#3f86d6;font-family:'Roboto Condensed',sans-serif;font-weight:700;font-size:15px;text-decoration:underline;text-underline-offset:4px}
.foot-link{position:absolute;left:334px;color:var(--white);font-size:12px}
.foot-contact{position:absolute;left:618px;display:flex;gap:14px;color:var(--white);font-size:12px;line-height:19px}
.social{position:absolute;top:3837px;width:32px;height:32px;border-radius:50%}
.copyright{left:0;top:4044px;width:1200px;height:49px;background:var(--red);color:var(--white);font-size:12px;display:flex;align-items:center;justify-content:center}
</style>
</head>
<body>

<!-- header -->
<div class="abs topbar"></div>
<div class="abs brand"><span class="brand-mark"></span><span class="brand-name">Bramblecourt<br>Electric</span></div>
<div class="abs hotline">
  <span class="hotline-icon"><svg width="16" height="16" viewBox="0 0 24 24" fill="#fff"><path d="M6.6 10.8a15.1 15.1 0 006.6 6.6l2.2-2.2a1 1 0 011-.25 11.4 11.4 0 003.6.57 1 1 0 011 1V20a1 1 0 01-1 1A17 17 0 013 4a1 1 0 011-1h3.5a1 1 0 011 1 11.4 11.4 0 00.57 3.6 1 1 0 01-.25 1z"/></svg></span>
  <div><small>Fast 24/7 service Available At No Extra Charge</small><strong>555 204 781</strong></div>
</div>
<nav class="abs nav">
  <a class="active" style="left:321px">HOME</a>
  <a style="left:463px">COMPANY</a>
  <a style="left:584px">SERVICES AREA</a>
  <a style="left:731px">SERVICES</a>
  <a style="left:843px">CONTACT</a>
  <a style="left:961px">GALLERY</a>
  <a style="left:1071px">FAQS</a>
</nav>

<!-- hero -->
<div class="abs hero"></div>
<div class="abs hero-photo" role="img" aria-label="Electrician in a hard hat drilling into a white brick wall socket"></div>
<h1 class="abs head hero-title">Bramblecourt<br><span class="accent">Electric Services</span></h1>
<p class="abs hero-text">Lorem Ipsum is simply dummy text of the printing and typesetting industry.<br>Lorem Ipsum has been the industry's standard dummy text</p>
<a class="btn" style="left:60px;top:493px;width:161px;height:35px">Contact Us Today</a>

<!-- connect band -->
<div class="abs connect"></div>
<svg class="abs connect-label" width="260" height="73" viewBox="0 0 260 73"><polygon points="0,0 237,0 258,36.5 237,73 0,73" fill="#1e63b4"/></svg>
<div class="abs connect-text">GET CONNECT WITH<br>US NOW</div>
<div class="field" style="left:289px;width:188px">Name*</div>
<div class="field" style="left:488px;width:187px">E-mail*</div>
<div class="field" style="left:686px;width:151px">Phone No.*</div>
<div class="field field-select" style="left:849px;width:187px">Service For*<svg width="12" height="8" viewBox="0 0 12 8"><path d="M1 1l5 5 5-5" stroke="#333" stroke-width="1.6" fill="none"/></svg></div>
<a class="btn connect-submit">Submit</a>

<!-- welcome -->
<div class="abs welcome-photo" role="img" aria-label="Engineer in a yellow hard hat checking an electrical control cabinet"></div>
<div class="abs play"><svg width="14" height="14" viewBox="0 0 14 14"><polygon points="3,1 13,7 3,13" fill="#fff"/></svg></div>
<h2 class="abs head welcome-title">Welcome to <span class="accent">Bramblecourt<br>Electric</span></h2>
<p class="abs welcome-text">Lorem Ipsum is simply dummy text of the printing and typesetting industry. Lorem Ipsum has been the industry's standard dummy text ever since the 1500s, when an unknown printer took a galley of type and scrambled it to make a type specimen book. It has survived not only five centuries, but also the leap into electronic typesetting, remaining essentially unchanged. It was popularised in the 1960s with the release of Letraset sheets containing Lorem Ipsum passages.</p>
<a class="btn" style="left:616px;top:1127px;width:115px;height:36px">Learn More</a>

<!-- services -->
<svg class="abs services-wave" viewBox="0 0 1200 740" preserveAspectRatio="none">
  <path d="M0 92 C 220 10, 420 10, 640 60 S 1030 70, 1200 6 L1200 660 C 1000 610, 800 600, 600 655 S 200 710, 0 730 Z" fill="#a3212a"/>
  <path d="M0 92 C 220 10, 420 10, 640 60 S 1030 70, 1200 6" stroke="#1e63b4" stroke-width="6" fill="none"/>
  <path d="M1200 660 C 1000 610, 800 600, 600 655 S 200 710, 0 730" stroke="#1e63b4" stroke-width="6" fill="none"/>
</svg>
<h2 class="abs head services-title">Our Services</h2>
<p class="abs services-intro">Lorem Ipsum is simply dummy text of the printing and typesetting industry.<br>Lorem Ipsum has been the industry's standard dummy text</p>
<div class="service" style="left:88px">
  <div class="service-photo" role="img" aria-label="Technician working on a commercial electrical panel"></div>
  <h3>Commerical Electrical Services</h3>
  <p>Lorem Ipsum is simply dummy text of the<br>printing and typesetting industry.</p>
  <div class="more">Learn More <svg width="24" height="10" viewBox="0 0 24 10"><path d="M0 5h20M15 1l5 4-5 4M11 1l5 4-5 4" stroke="#3f86d6" stroke-width="1.4" fill="none"/></svg></div>
</div>
<div class="service" style="left:434px">
  <div class="service-photo" role="img" aria-label="Electrician installing a residential wall socket"></div>
  <h3>Residential Electrical Services</h3>
  <p>Lorem Ipsum is simply dummy text of the<br>printing and typesetting industry.</p>
  <div class="more">Learn More <svg width="24" height="10" viewBox="0 0 24 10"><path d="M0 5h20M15 1l5 4-5 4M11 1l5 4-5 4" stroke="#3f86d6" stroke-width="1.4" fill="none"/></svg></div>
</div>
<div class="service" style="left:776px">
  <div class="service-photo" role="img" aria-label="Electrician wiring an industrial distribution board"></div>
  <h3>Industrial Electrical Services</h3>
  <p>Lorem Ipsum is simply dummy text of the<br>printing and typesetting industry.</p>
  <div class="more">Learn More <svg width="24" height="10" viewBox="0 0 24 10"><path d="M0 5h20M15 1l5 4-5 4M11 1l5 4-5 4" stroke="#3f86d6" stroke-width="1.4" fill="none"/></svg></div>
</div>

<!-- service area -->
<h2 class="abs head area-title">Services <span class="accent">Area</span></h2>
<p class="abs area-text">Lorem Ipsum is simply dummy text of the printing and typesetting industry. Lorem Ipsum has been the industry's standard dummy text ever since the 1500s, when an unknown printer took a galley of type.</p>
<div class="town" style="left:60px;top:2273px"><svg width="16" height="20" viewBox="0 0 16 20"><path d="M8 1a6 6 0 00-6 6c0 4.5 6 10 6 10s6-5.5 6-10a6 6 0 00-6-6z" stroke="#a3212a" stroke-width="2" fill="none"/><circle cx="8" cy="7" r="2.2" fill="#a3212a"/><path d="M2 19h12" stroke="#a3212a" stroke-width="2"/></svg>Moorhead</div>
<div class="town" style="left:219px;top:2273px"><svg width="16" height="20" viewBox="0 0 16 20"><path d="M8 1a6 6 0 00-6 6c0 4.5 6 10 6 10s6-5.5 6-10a6 6 0 00-6-6z" stroke="#a3212a" stroke-width="2" fill="none"/><circle cx="8" cy="7" r="2.2" fill="#a3212a"/><path d="M2 19h12" stroke="#a3212a" stroke-width="2"/></svg>Perham</div>
<div class="town" style="left:362px;top:2273px"><svg width="16" height="20" viewBox="0 0 16 20"><path d="M8 1a6 6 0 00-6 6c0 4.5 6 10 6 10s6-5.5 6-10a6 6 0 00-6-6z" stroke="#a3212a" stroke-width="2" fill="none"/><circle cx="8" cy="7" r="2.2" fill="#a3212a"/><path d="M2 19h12" stroke="#a3212a" stroke-width="2"/></svg>Ferguss Falls</div>
<div class="town" style="left:60px;top:2321px"><svg width="16" height="20" viewBox="0 0 16 20"><path d="M8 1a6 6 0 00-6 6c0 4.5 6 10 6 10s6-5.5 6-10a6 6 0 00-6-6z" stroke="#a3212a" stroke-width="2" fill="none"/><circle cx="8" cy="7" r="2.2" fill="#a3212a"/><path d="M2 19h12" stroke="#a3212a" stroke-width="2"/></svg>Alexandria</div>
<div class="town" style="left:219px;top:2321px"><svg width="16" height="20" viewBox="0 0 16 20"><path d="M8 1a6 6 0 00-6 6c0 4.5 6 10 6 10s6-5.5 6-10a6 6 0 00-6-6z" stroke="#a3212a" stroke-width="2" fill="none"/><circle cx="8" cy="7" r="2.2" fill="#a3212a"/><path d="M2 19h12" stroke="#a3212a" stroke-width="2"/></svg>Little Falls</div>
<a class="btn" style="left:60px;top:2391px;width:116px;height:37px">Learn More</a>
<div class="abs area-map" role="img" aria-label="Map of the state's counties grouped into service zones"></div>

<!-- gallery -->
<svg class="abs gallery-bg" viewBox="0 0 1200 620" preserveAspectRatio="none">
  <path d="M0 80 C 200 10, 420 0, 640 50 S 1030 60, 1200 6 L1200 620 L0 620 Z" fill="#f5f5f5"/>
  <path d="M0 80 C 200 10, 420 0, 640 50 S 1030 60, 1200 6" stroke="#1e63b4" stroke-width="6" fill="none"/>
</svg>
<h2 class="abs head gallery-title">Project <span class="accent">Gallery</span></h2>
<p class="abs gallery-text">Lorem Ipsum is simply dummy text of the printing and typesetting industry.<br>Lorem Ipsum has been the industry's standard dummy text</p>
<div class="shot" style="left:0;width:284px;background:linear-gradient(180deg,#e9e1d2,#a88a63 70%,#6e5238)" role="img" aria-label="Warmly lit bedroom interior"></div>
<div class="shot" style="left:305px;width:285px;background:linear-gradient(180deg,#e8e8e8,#bdbdbd 60%,#7d7f82)" role="img" aria-label="Modern white reception lobby"></div>
<div class="shot" style="left:609px;width:284px;background:linear-gradient(180deg,#3f5778,#6d7d90 55%,#4a4d52)" role="img" aria-label="Industrial warehouse building at dusk"></div>
<div class="abs" style="left:733px;top:2886px;width:36px;height:36px;border-radius:50%;border:1.5px solid #fff;display:flex;align-items:center;justify-content:center"><svg width="14" height="14" viewBox="0 0 14 14"><path d="M7 0v14M0 7h14" stroke="#fff" stroke-width="1.5"/></svg></div>
<div class="shot" style="left:914px;width:286px;background:linear-gradient(180deg,#dfe6ee,#a98a6a 60%,#6f7a66)" role="img" aria-label="Modern office building with timber facade"></div>
<div class="arrow" style="left:44px;background:var(--red)"><svg width="10" height="12" viewBox="0 0 10 12"><path d="M7 1L2 6l5 5" stroke="#fff" stroke-width="1.8" fill="none"/></svg></div>
<div class="arrow" style="left:1123px;background:var(--ink)"><svg width="10" height="12" viewBox="0 0 10 12"><path d="M3 1l5 5-5 5" stroke="#fff" stroke-width="1.8" fill="none"/></svg></div>
<a class="btn" style="left:500px;top:3068px;width:199px;height:35px">View Our Project Gallery</a>

<!-- contact -->
<h2 class="abs head contact-title">Contact <span class="accent">Us</span></h2>
<p class="abs contact-sub">Have An any quetions for Contact Us Today!</p>
<div class="input focus" style="top:3321px">Name*</div>
<div class="input" style="top:3375px">E-mail*</div>
<div class="input" style="top:3429px">Phone No.*</div>
<div class="input" style="top:3477px">Subject*</div>
<div class="input" style="left:612px;top:3321px;height:191px">Massage*</div>
<a class="btn" style="left:555px;top:3551px;width:90px;height:37px">Submit</a>

<!-- footer -->
<svg class="abs footer-wave" viewBox="0 0 1200 400" preserveAspectRatio="none">
  <path d="M0 80 C 200 10, 420 0, 640 60 S 1030 70, 1200 10 L1200 400 L0 400 Z" fill="#000"/>
  <path d="M0 80 C 200 10, 420 0, 640 60 S 1030 70, 1200 10" stroke="#1e63b4" stroke-width="6" fill="none"/>
</svg>
<div class="abs foot-brand"><span class="brand-mark"></span><span>Bramblecourt<br>Electric</span></div>
<div class="foot-head" style="left:334px">SITE MAP</div>
<div class="foot-link" style="top:3829px">Company</div>
<div class="foot-link" style="top:3861px">Services Area</div>
<div class="foot-link" style="top:3893px">Services</div>
<div class="foot-link" style="top:3924px">Contact</div>
<div class="foot-link" style="top:3956px">Gallery</div>
<div class="foot-link" style="top:3989px">Faqs</div>
<div class="foot-head" style="left:618px">CONTACT US</div>
<div class="foot-contact" style="top:3836px"><svg width="16" height="18" viewBox="0 0 16 20"><path d="M8 1a6 6 0 00-6 6c0 4.5 6 10 6 10s6-5.5 6-10a6 6 0 00-6-6z" stroke="#fff" stroke-width="2" fill="none"/><circle cx="8" cy="7" r="2" fill="#fff"/></svg><span>1420 Larkspur Ave NE Fenwick, MN<br>55990</span></div>
<div class="foot-contact" style="top:3890px"><svg width="16" height="16" viewBox="0 0 24 24" fill="#fff"><path d="M6.6 10.8a15.1 15.1 0 006.6 6.6l2.2-2.2a1 1 0 011-.25 11.4 11.4 0 003.6.57 1 1 0 011 1V20a1 1 0 01-1 1A17 17 0 013 4a1 1 0 011-1h3.5a1 1 0 011 1 11.4 11.4 0 00.57 3.6 1 1 0 01-.25 1z"/></svg><span>555 204 781</span></div>
<div class="foot-contact" style="top:3925px"><svg width="16" height="14" viewBox="0 0 16 12"><rect x="0.5" y="0.5" width="15" height="11" fill="#fff"/><path d="M1 1l7 6 7-6" stroke="#000" stroke-width="1.2" fill="none"/></svg><span>info@bramblecourtelectric.com</span></div>
<div class="foot-head" style="left:891px">FOLLOW ON US</div>
<div class="social" style="left:890px;background:var(--blue)"></div>
<div class="social" style="left:937px;background:var(--white)"></div>
<div class="social" style="left:985px;background:var(--white)"></div>
<div class="abs copyright">© Copyright 2022 Bramblecourt Electric.All Right Reserved.</div>

</body>
</html>
```